Marla Tovesby, Broker Associate

I need a new business card for my Real Estate services. I am a Broker Associate and also have my MBA. I am a PA too. I would like to have it say "Third Generation Selling" too some where. I like the bold look of cards and I think I am leaning towards a black or dark background. I need it to tie in my logo with the Pinegate Marsden Vic Olander Realty logo. I like the foil and shiny look of some letters too. I might add my picture but would like to see some with out my picture too. I sell a lot of lakefront homes but I don't want it to be focused on water. Maybe subtle?

Target Market(s)

18+

Industry/Entity Type

Real Estate Agent

Contact Information for Business Card

The design must have my logo and Pinegate Marsden logo.
My name: Marla Tovesby
My cell phone 555-318-2976
business address: 4820 West Orchard Road Brindlewood, FL 32968
Office phone: 555-762-0158
email: MarlaJTovesby@mailbrook.test
website: www.BrightporchHomes.test
Facebook: www.facebook.com/marlabrightporchhomes
Also 'Third Generation Selling' and Realtor logo must be on it.

Font styles to use
Sans Serif

Colors
0555a3
000000
ffffff
d3d3d3
3176b5

Requirements
Must have
• I want this to stand out from all the other Realtors. I like bold look. I need it to match my logo and tie in the Pinegate Marsden logo. I can do front and back on card. The office details can be smaller than my name and information.
Nice to have
• I like the foil look and matte as well. I want something bold that stands out.

```html
<!DOCTYPE html>
<html lang="en">
<head>
<meta charset="utf-8">
<title>Marla Tovesby – Business Card</title>
<link rel="stylesheet" href="https://fonts.googleapis.com/css2?family=Lato:wght@400;700;900&family=Arimo:wght@400&display=swap">
<style>
  :root {
    --page-bg: #e9e9ea;
    --panel-dark: #333435;
    --accent-blue: #1c7ad1;
    --brand-navy: #0555a3;
    --ink: #2d2d2f;
    --white: #ffffff;
    --light-grey: #d3d3d3;
    --rule: #4a4b4d;
  }
  * { margin: 0; padding: 0; box-sizing: border-box; }
  html, body {
    width: 1200px; height: 900px; overflow: hidden;
    background: var(--page-bg);
  }
  .card {
    position: absolute; left: 120px; top: 153px;
    width: 960px; height: 594px;
    display: flex;
    box-shadow: 0 6px 24px rgba(0,0,0,.18);
    overflow: hidden;
  }
  .contact-panel {
    position: relative; width: 474px; height: 100%;
    background: var(--panel-dark);
    color: var(--white);
    font-family: "Arimo", Arial, sans-serif;
  }
  .divider {
    position: absolute; left: 474px; top: 0; width: 7px; height: 100%;
    background: var(--accent-blue); z-index: 2;
  }
  .divider-notch {
    position: absolute; left: 464px; top: 104px; z-index: 2;
  }
  .brand-panel {
    position: relative; flex: 1; height: 100%;
    background: linear-gradient(135deg, #f7f7f7 0%, #eeeeef 55%, #e4e4e6 100%);
  }
  .line { position: absolute; right: 37px; white-space: nowrap; text-align: right; line-height: 1; }
  .line.with-icon { right: 64px; }
  .agent-name {
    top: 84px; font-family: "Lato", sans-serif; font-weight: 700;
    font-size: 36px; color: var(--accent-blue); letter-spacing: .3px;
  }
  .agent-title { top: 123px; font-size: 25px; color: #e6e6e6; }
  .address { font-size: 26px; color: #f2f2f2; }
  .address.street { top: 177px; }
  .address.city { top: 211px; }
  .detail { font-size: 25px; color: #f2f2f2; }
  .detail.office { top: 258px; }
  .detail.cell { top: 292px; }
  .detail.email { top: 326px; }
  .detail.web { top: 361px; }
  .detail.social { top: 412px; font-size: 27px; right: 78px; }
  .icon { position: absolute; right: 37px; width: 20px; height: 20px; }
  .icon.office { top: 261px; }
  .icon.cell { top: 294px; }
  .icon.email { top: 330px; }
  .icon.web { top: 364px; }
  .social-dot {
    position: absolute; right: 37px; top: 411px; width: 30px; height: 30px;
    border-radius: 50%; background: var(--white);
  }
  .rule {
    position: absolute; left: 42px; right: 37px; top: 463px;
    height: 1px; background: var(--rule);
  }
  .tagline {
    top: 487px; font-family: "Lato", sans-serif; font-weight: 700;
    font-size: 27px; color: var(--white); letter-spacing: .4px;
  }
  .agent-mark {
    position: absolute; left: 0; right: 0; top: 250px;
    display: flex; align-items: center; justify-content: center; gap: 14px;
  }
  .agent-mark-square { width: 30px; height: 30px; background: var(--brand-navy); }
  .agent-mark-name {
    font-family: "Lato", sans-serif; font-weight: 900; font-size: 42px;
    color: var(--ink); letter-spacing: .5px;
  }
  .office-badge {
    position: absolute; left: 148px; top: 375px; width: 190px; height: 82px;
    background: linear-gradient(#1e4ea6, #14367a);
    border: 3px solid #dfe3ea;
  }
  .office-name {
    position: absolute; left: 0; right: 0; text-align: center;
    font-family: "Lato", sans-serif; font-weight: 900; font-size: 22px;
    color: #111; letter-spacing: .5px;
  }
  .office-name.top { top: 476px; }
  .office-name.bottom { top: 505px; }
</style>
</head>
<body>
  <main class="card">
    <section class="contact-panel">
      <p class="line agent-name">MARLA TOVESBY</p>
      <p class="line agent-title">Broker Associate</p>

      <p class="line address street">4820 West Orchard Road</p>
      <p class="line address city">Brindlewood, FL 32968</p>

      <p class="line with-icon detail office">555-762-0158</p>
      <svg class="icon office" viewBox="0 0 20 20" aria-hidden="true"><path fill="#1c7ad1" d="M2 8c0-3 3-5 8-5s8 2 8 5l-4 1-1-2H7L6 9zM5 10h10l2 7H3z"/><circle cx="10" cy="13.5" r="2" fill="#333435"/></svg>

      <p class="line with-icon detail cell">555-318-2976</p>
      <svg class="icon cell" viewBox="0 0 20 20" aria-hidden="true"><rect x="5" y="1" width="10" height="18" rx="2" fill="none" stroke="#1c7ad1" stroke-width="2"/><circle cx="10" cy="15.5" r="1.2" fill="#1c7ad1"/></svg>

      <p class="line with-icon detail email">MarlaJTovesby@mailbrook.test</p>
      <svg class="icon email" viewBox="0 0 20 20" aria-hidden="true"><rect x="1" y="4" width="18" height="12" fill="#1c7ad1"/><path d="M1 4l9 7 9-7" fill="none" stroke="#333435" stroke-width="1.5"/></svg>

      <p class="line with-icon detail web">www.BrightporchHomes.test</p>
      <svg class="icon web" viewBox="0 0 20 20" aria-hidden="true"><circle cx="10" cy="10" r="8.5" fill="#1c7ad1"/><path d="M1.5 10h17M10 1.5c-3 3-3 14 0 17M10 1.5c3 3 3 14 0 17" fill="none" stroke="#333435" stroke-width="1.2"/></svg>

      <p class="line detail social">/marlabrightporchhomes</p>
      <span class="social-dot" aria-hidden="true"></span>

      <div class="rule"></div>
      <p class="line tagline">THIRD GENERATION SELLING</p>
    </section>

    <div class="divider" aria-hidden="true"></div>
    <svg class="divider-notch" width="12" height="34" viewBox="0 0 12 34" aria-hidden="true"><path d="M12 0L0 17l12 17z" fill="#1c7ad1"/></svg>

    <section class="brand-panel">
      <div class="agent-mark">
        <span class="agent-mark-square" aria-hidden="true"></span>
        <span class="agent-mark-name">MARLA TOVESBY</span>
      </div>
      <div class="office-badge" role="img" aria-label="Pinegate Marsden brokerage badge"></div>
      <p class="office-name top">VIC OLANDER</p>
      <p class="office-name bottom">REALTY</p>
    </section>
  </main>
</body>
</html>
```